Sheriff Candidate needs a large yard sign

A candidate for Sheriff needs to have a sign to put in front of businesses and houses that advertise her candidacy.

Target Market(s)

Democrats, voters

Industry/Entity Type

Political

Font styles to use
Sans Serif

Colors
34a7d7
3276b5

Requirements
Must have
• Must have her picture
• Must have the words "Elect Dana Holloway" - I'd like the name Dana to be smaller Holloway. "Elect" and "Holloway" should be the focus.
• at the bottom in a box "Paid for by the Committee to Elect Dana Holloway"
Nice to have
• it would be good to have her logo as well.
• blue color for democrats and on a white background
Should not have
• pink color

```html
<!DOCTYPE html>
<html lang="en">
<head>
<meta charset="utf-8">
<title>Elect Dana Holloway – Yard Sign</title>
<link rel="stylesheet" href="https://fonts.googleapis.com/css2?family=Fira+Sans+Extra+Condensed:wght@300;400;600;700&display=swap">
<style>
  :root {
    --sky-blue: #34a7d7;
    --party-blue: #3276b5;
    --ink: #0b0b0b;
    --paper: #ffffff;
    --backdrop: #e8ebee;
    --accent-gray: #555352;
    --badge-gold: #c9a23a;
    --photo-light: #8c8987;
    --photo-dark: #5b5857;
  }
  html, body {
    margin: 0;
    width: 1200px;
    height: 1000px;
    overflow: hidden;
    background: var(--backdrop);
  }
  .canvas {
    position: relative;
    width: 1200px;
    height: 1000px;
  }
  .yard-sign {
    position: absolute;
    left: 20px;
    top: 174px;
    width: 1465px;
    height: 823px;
    transform: scale(0.792);
    transform-origin: top left;
    background: var(--paper);
    overflow: hidden;
    font-family: "Fira Sans Extra Condensed", "Arial Narrow", sans-serif;
    box-shadow: 0 10px 30px rgba(0,0,0,0.15);
  }
  .sign-shapes {
    position: absolute;
    inset: 0;
  }
  .sign-text {
    position: absolute;
    margin: 0;
    line-height: 1;
    white-space: nowrap;
  }
  .campaign-mark {
    position: absolute;
    left: 270px;
    top: 40px;
    width: 260px;
    height: 250px;
    display: flex;
    flex-direction: column;
    align-items: center;
    justify-content: center;
    gap: 14px;
  }
  .campaign-mark .mark-dot {
    width: 64px;
    height: 64px;
    border-radius: 50%;
    background: var(--badge-gold);
  }
  .campaign-mark .mark-name {
    color: var(--party-blue);
    font-weight: 600;
    font-size: 36px;
    line-height: 1.05;
    text-align: center;
    letter-spacing: 1px;
    text-transform: uppercase;
  }
  .headline-elect {
    left: 60px;
    top: 306px;
    color: var(--party-blue);
    font-weight: 700;
    font-size: 150px;
  }
  .headline-first {
    position: absolute;
    left: 130px;
    top: 445px;
    width: 514px;
    display: flex;
    align-items: center;
    gap: 12px;
  }
  .headline-first .rule-set {
    flex: 1;
    height: 37px;
    background:
      linear-gradient(var(--party-blue), var(--party-blue)) 0 0 / 100% 2px no-repeat,
      linear-gradient(var(--party-blue), var(--party-blue)) 0 17px / 100% 2px no-repeat,
      linear-gradient(var(--party-blue), var(--party-blue)) 0 35px / 100% 2px no-repeat;
  }
  .headline-first .first-name {
    color: var(--sky-blue);
    font-weight: 300;
    font-size: 87px;
    line-height: 1;
  }
  .headline-last {
    left: 150px;
    top: 526px;
    color: var(--party-blue);
    font-weight: 700;
    font-size: 120px;
    letter-spacing: -1px;
  }
  .tagline {
    left: 28px;
    top: 669px;
    color: var(--paper);
    font-weight: 600;
    font-size: 52px;
    letter-spacing: 1px;
  }
  .party-label {
    left: 540px;
    top: 669px;
    color: var(--party-blue);
    font-weight: 600;
    font-size: 52px;
  }
  .disclaimer {
    left: 36px;
    top: 750px;
    display: flex;
    align-items: baseline;
    gap: 12px;
    color: var(--paper);
  }
  .disclaimer .lead {
    font-weight: 400;
    font-size: 36px;
  }
  .disclaimer .committee {
    font-weight: 600;
    font-size: 52px;
  }
</style>
</head>
<body>
<main class="canvas">
  <section class="yard-sign" aria-label="Campaign yard sign for sheriff">
    <svg class="sign-shapes" viewBox="0 0 1465 823" width="1465" height="823">
      <defs>
        <linearGradient id="portraitTone" x1="0" y1="0" x2="1" y2="1">
          <stop offset="0" stop-color="#8c8987"/>
          <stop offset="1" stop-color="#5b5857"/>
        </linearGradient>
      </defs>
      <path d="M0,0 H900 V70 Q620,120 0,105 Z" fill="#34a7d7"/>
      <circle cx="400" cy="163" r="145" fill="#ffffff"/>
      <path d="M0,718 H900 L960,823 H0 Z" fill="#34a7d7"/>
      <path d="M0,660 H500 L530,718 H0 Z" fill="#0b0b0b"/>
      <rect x="500" y="713" width="310" height="6" fill="#0b0b0b"/>
      <path d="M860,20 C700,260 700,560 900,760" fill="none" stroke="#3276b5" stroke-width="7"/>
      <path d="M885,15 C730,260 735,560 930,800" fill="none" stroke="#555352" stroke-width="9"/>
      <path d="M905,0 H1465 V823 H955 C770,680 730,340 905,0 Z" fill="url(#portraitTone)" role="img" aria-label="Portrait photograph of the candidate in a dark blazer"/>
    </svg>

    <div class="campaign-mark">
      <span class="mark-dot" aria-hidden="true"></span>
      <span class="mark-name">Holloway<br>for Sheriff</span>
    </div>

    <h1 class="sign-text headline-elect">ELECT</h1>
    <div class="headline-first">
      <span class="rule-set" aria-hidden="true"></span>
      <span class="first-name">DANA</span>
      <span class="rule-set" aria-hidden="true"></span>
    </div>
    <h2 class="sign-text headline-last">HOLLOWAY</h2>

    <div class="sign-text tagline">COMMUNITY POLICING</div>
    <div class="sign-text party-label">DEMOCRAT</div>

    <p class="sign-text disclaimer">
      <span class="lead">Paid for by the Committee to</span>
      <span class="committee">ELECT DANA HOLLOWAY</span>
    </p>
  </section>
</main>
</body>
</html>
```